Visitenkarte erstellen für Reiki Praxis

Visitenkarten für Reiki Praxis Doppelseitig

business cards reiki practice double-sided

The background can also be a different color

```html
<!DOCTYPE html>
<html lang="en">
<head>
<meta charset="UTF-8">
<title>Lumen Reiki – Business Cards</title>
<link href="https://fonts.googleapis.com/css2?family=Montserrat:wght@400;500;700;800&display=swap" rel="stylesheet">
<style>
  :root {
    --backdrop: #ece6df;
    --card-black: #030303;
    --card-white: #ffffff;
    --ink: #111111;
    --text-light: #ffffff;
    --gold: #e0a31c;
    --blush: #c98a8a;
    --peach: #f1c7a3;
    --shadow: rgba(0, 0, 0, 0.28);
  }
  * { box-sizing: border-box; margin: 0; padding: 0; }
  html, body {
    width: 1200px;
    height: 1000px;
    overflow: hidden;
    background: var(--backdrop);
    font-family: "Montserrat", sans-serif;
  }
  .canvas {
    position: relative;
    width: 1200px;
    height: 1000px;
  }
  .card {
    position: absolute;
    left: 290px;
    width: 620px;
    height: 354px;
    box-shadow: 0 10px 24px var(--shadow);
    overflow: hidden;
  }
  .card--front { top: 116px; display: flex; }
  .card--back { top: 530px; background: var(--card-black); }

  /* front: brand panel */
  .brand-panel {
    position: relative;
    width: 268px;
    height: 100%;
    background: var(--card-black);
  }
  .brand-panel .gold-rule {
    position: absolute;
    right: 12px;
    top: 0;
    width: 2px;
    height: 98px;
    background: var(--gold);
  }
  .divider-strip {
    width: 5px;
    height: 100%;
    background: linear-gradient(to bottom, var(--blush), var(--peach));
  }

  .brand-mark {
    position: absolute;
    left: 0;
    right: 0;
    display: flex;
    flex-direction: column;
    align-items: center;
    gap: 12px;
  }
  .brand-panel .brand-mark { top: 150px; }
  .card--back .brand-mark { top: 140px; }
  .brand-mark .mark-dot {
    width: 22px;
    height: 22px;
    border-radius: 50%;
    background: var(--gold);
  }
  .brand-mark .brand-name {
    color: var(--text-light);
    font-weight: 500;
    letter-spacing: 0.5px;
    white-space: nowrap;
  }
  .brand-panel .brand-name { font-size: 18px; }
  .card--back .brand-name { font-size: 21px; }

  /* front: contact panel */
  .contact-panel {
    position: relative;
    flex: 1;
    background: var(--card-white);
    color: var(--ink);
    padding: 54px 0 0 32px;
  }
  .person-name {
    font-size: 22px;
    font-weight: 800;
    letter-spacing: -0.3px;
    line-height: 1;
  }
  .person-role {
    font-size: 10px;
    font-weight: 700;
    margin-top: 4px;
    margin-left: 6px;
  }
  .contact-list {
    list-style: none;
    margin-top: 40px;
    margin-left: 20px;
  }
  .contact-list li {
    display: flex;
    align-items: flex-start;
    gap: 10px;
    font-size: 12.5px;
    font-weight: 400;
    line-height: 1.3;
    margin-bottom: 12px;
  }
  .contact-list svg {
    flex: 0 0 12px;
    width: 12px;
    height: 12px;
    margin-top: 2px;
    fill: var(--ink);
  }
  .contact-panel .ink-rule {
    position: absolute;
    left: 14px;
    bottom: 0;
    width: 2px;
    height: 96px;
    background: var(--ink);
  }
</style>
</head>
<body>
<main class="canvas">

  <section class="card card--front" aria-label="Business card front">
    <div class="brand-panel">
      <span class="gold-rule"></span>
      <div class="brand-mark">
        <span class="mark-dot"></span>
        <span class="brand-name">LUMEN REIKI</span>
      </div>
    </div>
    <div class="divider-strip"></div>
    <div class="contact-panel">
      <h1 class="person-name">JOHN DOE</h1>
      <p class="person-role">DESIGNATION</p>
      <ul class="contact-list">
        <li>
          <svg viewBox="0 0 12 12" aria-hidden="true"><path d="M6 0a4 4 0 0 0-4 4c0 3 4 8 4 8s4-5 4-8a4 4 0 0 0-4-4zm0 5.5A1.5 1.5 0 1 1 6 2.5a1.5 1.5 0 0 1 0 3z"/></svg>
          <span>48 Willow Lane Area,<br>CO- 80211</span>
        </li>
        <li>
          <svg viewBox="0 0 12 12" aria-hidden="true"><path d="M2.4 0.5l2 2.2-1 1.4c.8 1.7 2 2.9 3.6 3.7l1.4-1 2.1 2-1.2 2.2C4.7 11.2.8 7.3.5 1.7z"/></svg>
          <span>555-014-2290</span>
        </li>
        <li>
          <svg viewBox="0 0 12 12" aria-hidden="true"><path d="M0 2h12v8H0zm1 1v.3l5 3.3 5-3.3V3z"/></svg>
          <span>lumenreiki@mailbox.com</span>
        </li>
        <li>
          <svg viewBox="0 0 12 12" aria-hidden="true"><path d="M6 0a6 6 0 1 0 0 12A6 6 0 0 0 6 0zm4.9 5.4H8.6A9 9 0 0 0 7.4 1.2a5 5 0 0 1 3.5 4.2zM6 1.1c.8 1 1.4 2.6 1.5 4.3h-3C4.6 3.7 5.2 2.1 6 1.1zM4.6 1.2a9 9 0 0 0-1.2 4.2H1.1a5 5 0 0 1 3.5-4.2zM1.1 6.6h2.3a9 9 0 0 0 1.2 4.2 5 5 0 0 1-3.5-4.2zM6 10.9c-.8-1-1.4-2.6-1.5-4.3h3c-.1 1.7-.7 3.3-1.5 4.3zm1.4-.1a9 9 0 0 0 1.2-4.2h2.3a5 5 0 0 1-3.5 4.2z"/></svg>
          <span>www.lumenreiki.com</span>
        </li>
      </ul>
      <span class="ink-rule"></span>
    </div>
  </section>

  <section class="card card--back" aria-label="Business card back">
    <div class="brand-mark">
      <span class="mark-dot"></span>
      <span class="brand-name">LUMEN REIKI</span>
    </div>
  </section>

</main>
</body>
</html>
```